Post Card Invitation to Wedding Rehearsal Dinner and After Party

This post card should serve as invitations for two events in the wedding weekend for two San Francisco grooms, Derek and Simon.
Each side of the card should have distinct looks and information but tied together with “Before” on the front and “After” on the back.
POST CARD FRONT
Required text:
BEFORE
Derek and Simon’s Wedding: Rehearsal Dinner
Friday, May 22, 2015
5:30 PM
Larkvale Grub Yard
617 Tessler Avenue @ Marlow
San Francisco, CA
Please also convey the following information without necessarily quoting directly: This rehearsal dinner will be held in a private enclosed space in the food truck park. We we will serve beer and wine in our space and provide tickets to purchase food from any of the trucks in the park. Dress is casual.
Look and feel of the card should have a modern, “hipster” feel to it. If you search Google images for “Hipster design” or “hipster infographic” you should get a sense of the overall design and colors. The website for the venue is http://larkvalegrubyard.com/ for reference but please DO NOT use any images or logos from the site.
----------------------
POST CARD REVERSE
Required Text:
AFTER
Derek and Simon’s Wedding: After Party
Saturday, May 23, 2015
7:30 PM
Corvell Harbor Sailing Club
42 Pennick Lane
San Francisco, CA
Please also convey the following information without necessarily quoting directly: Black-tie optional. Dancing, snacks and dessert and cocktails with panoramic views of the San Francisco Bay and Golden Gate Bridge.
This should have a much different look and feel from the front of the card. It should convey an elegant black-tie affair. If you search Google images for “black tie after party invitation” you should get some examples of an overall feel that I am aiming for. The website for the venue is www.chsclub.com but DO NOT use any of the images or logos from the site.
Industry/Entity Type
Wedding
Look and feel
Each slider illustrates characteristics of the customer's brand and the style your logo design should communicate.

```html
<!DOCTYPE html>
<html lang="en">
<head>
<meta charset="utf-8">
<title>Derek and Simon's Wedding – Rehearsal Dinner</title>
<link rel="stylesheet" href="https://fonts.googleapis.com/css2?family=Kaushan+Script&family=Lobster&family=Yesteryear&family=Dancing+Script:wght@600;700&display=swap">
<style>
  :root {
    --rust: #b1432a;
    --rust-deep: #9c3a24;
    --brown: #5e4a3c;
    --brown-dark: #4c3a2f;
    --brown-light: #7a6452;
    --cream: #f3ebc4;
    --teal: #80b59b;
    --teal-dark: #5e9079;
    --teal-shade: #4d7866;
  }
  html, body {
    margin: 0;
    padding: 0;
    width: 1200px;
    height: 779px;
    overflow: hidden;
    background: var(--rust);
  }
  .postcard {
    display: block;
    width: 1200px;
    height: 779px;
  }
  .postcard__bg { fill: var(--rust); }
  .corner-band { fill: var(--brown-dark); }
  .corner-label {
    font-family: "Kaushan Script", cursive;
    font-size: 74px;
    fill: var(--cream);
  }
  .badge__rim { fill: var(--cream); }
  .badge__field { fill: url(#badgeGlow); }
  .badge__line { fill: none; stroke: var(--cream); stroke-width: 3; opacity: .55; }
  .ribbon__band { fill: var(--teal); }
  .ribbon__fold { fill: var(--teal-shade); }
  .ribbon__tail { fill: var(--teal-dark); }
  .couple-names {
    font-family: "Lobster", cursive;
    font-size: 92px;
    fill: var(--rust);
    stroke: var(--cream);
    stroke-width: 3px;
    paint-order: stroke fill;
  }
  .event-title {
    font-family: "Yesteryear", cursive;
    font-size: 68px;
    fill: var(--cream);
  }
  .event-subtitle {
    font-family: "Yesteryear", cursive;
    font-size: 31px;
    fill: var(--cream);
  }
  .info-text {
    font-family: "Dancing Script", cursive;
    font-weight: 600;
    fill: var(--cream);
  }
  .info-text--date { font-size: 38px; }
  .info-text--venue { font-size: 34px; }
  .details-note {
    font-family: "Dancing Script", cursive;
    font-weight: 700;
    font-size: 19px;
    fill: var(--cream);
  }
</style>
</head>
<body>
<svg class="postcard" viewBox="0 0 1200 779" xmlns="http://www.w3.org/2000/svg">
  <defs>
    <radialGradient id="badgeGlow" cx="50%" cy="38%" r="65%">
      <stop offset="0%" stop-color="var(--brown-light)"/>
      <stop offset="100%" stop-color="var(--brown)"/>
    </radialGradient>
  </defs>

  <rect class="postcard__bg" width="1200" height="779"/>

  <!-- Corner band with "Before" -->
  <path class="corner-band" d="M0,0 H418 L0,244 Z"/>
  <text class="corner-label" x="150" y="118" text-anchor="middle" transform="rotate(-30 150 95)">BEFORE</text>

  <!-- Central badge -->
  <g class="badge" role="img" aria-label="Label-shaped badge with soft sunburst glow">
    <path class="badge__rim" d="M312,178 Q300,150 330,146 Q470,132 530,96 Q607,58 684,96 Q744,132 884,146 Q914,150 902,178 Q888,300 902,420 Q912,452 880,462 Q720,480 660,512 Q607,540 554,512 Q494,480 334,462 Q302,452 312,420 Q326,300 312,178 Z"/>
    <path class="badge__field" d="M330,182 Q322,162 344,160 Q478,146 540,112 Q607,78 674,112 Q736,146 870,160 Q892,162 884,182 Q872,300 884,414 Q890,440 866,446 Q712,464 650,494 Q607,516 564,494 Q502,464 348,446 Q324,440 330,414 Q342,300 330,182 Z"/>
    <path class="badge__line" d="M344,190 Q338,174 356,172 Q486,158 546,126 Q607,96 668,126 Q728,158 858,172 Q876,174 870,190 Q860,300 870,406 Q874,428 854,432 Q706,450 644,480 Q607,498 570,480 Q508,450 360,432 Q340,428 344,406 Q354,300 344,190 Z"/>
  </g>

  <!-- Name ribbon -->
  <g class="ribbon">
    <path class="ribbon__tail" d="M232,262 L290,262 L290,380 L232,380 L252,321 Z"/>
    <path class="ribbon__tail" d="M968,262 L910,262 L910,380 L968,380 L948,321 Z"/>
    <path class="ribbon__fold" d="M262,362 L290,380 L290,362 Z"/>
    <path class="ribbon__fold" d="M938,362 L910,380 L910,362 Z"/>
    <path class="ribbon__band" d="M262,236 Q600,206 938,236 L938,362 Q600,334 262,362 Z"/>
  </g>
  <text class="couple-names" x="600" y="326" text-anchor="middle">Derek and Simon’s</text>

  <text class="event-title" x="607" y="418" text-anchor="middle">Wedding</text>
  <text class="event-subtitle" x="600" y="462" text-anchor="middle">Rehearsal Dinner</text>

  <!-- Date banner -->
  <g class="banner banner--date">
    <path class="ribbon__fold" d="M350,661 L396,690 L396,661 Z"/>
    <path class="ribbon__band" d="M0,537 H396 L372,599 L396,661 H0 Z"/>
  </g>
  <text class="info-text info-text--date" x="44" y="590">Friday, May 22, 2015</text>
  <text class="info-text info-text--date" x="100" y="638">5:30 PM</text>

  <!-- Venue banner -->
  <g class="banner banner--venue">
    <path class="ribbon__fold" d="M806,695 L763,718 L763,695 Z"/>
    <path class="ribbon__band" d="M763,522 H1200 V695 H763 L800,608 Z"/>
  </g>
  <text class="info-text info-text--venue" x="812" y="576">Larkvale Grub Yard</text>
  <text class="info-text info-text--venue" x="812" y="618">617 Tessler Avenue @ Marlow</text>
  <text class="info-text info-text--venue" x="812" y="660">San Francisco, CA</text>

  <!-- Details -->
  <text class="details-note" x="600" y="725" text-anchor="middle">This rehearsal dinner will be held in a private enclosed space in the food truck park. We we will serve beer and</text>
  <text class="details-note" x="600" y="754" text-anchor="middle">wine in our space and provide tickets to purchase food from any of the trucks in the park. Dress is casual.</text>
</svg>
</body>
</html>
```